Garage Flooring Flyer

We are looking for a flyer design for our garage flooring company. We specialise in installing garage floor coatings. We use industrial grade products and are serious about durability and quality.
We target male car enthusiasts and want to project the image of a modern high-tech company. The flyer should be stunningly visual and incorporate the logo and photos we have attached. Other photos or images are welcomed.
Some key mentions to be made on the flyer are listed below:
About Us
"We are K*** R***** LLC, Home of the garage enthusiasts and Waukesha’s premier garage floor installer"
Services
Garage Floor Coatings
Offers
-Call or Email for a FREE estimate!
Credentials
-QN logo
-Pictavo Logo
-Zorbin Logo
-5stars?
Benefit Highlights to be mentioned or listed (not in any particular order)
-Industrial Quality and Strength
-Easy to Clean
-Many Color Options
-Locally Owned and Operated
-Satisfaction Guaranteed
-Lifetime Limited Warranty
-Increases Home Value
-MAKE YOUR FRIENDS AND NEIGHBORS JEALOUS!
-Fully Insured
-Certified and Trusted Installer
-Oil and Chemical Resistant
-UV Stable
-Impact and Abrasion Resistant
Contact Info
-Phone
-Email
-Website
Captions
-"From diamond grinding surface prep to using only the highest industrial-grade products, we believe in taking the time to ensure a proper installation and guarantee a durable long-lasting and beautiful garage floor";
-Serving Southeastern Wisconsin!

```html
<!DOCTYPE html>
<html lang="en">
<head>
<meta charset="utf-8">
<title>Kore Revive – Garage Flooring Flyer</title>
<link href="https://fonts.googleapis.com/css2?family=Oswald:wght@500;700&family=Nunito:wght@700;800&family=Open+Sans:wght@400;600&display=swap" rel="stylesheet">
<style>
  :root {
    --sky-light: #e4f5f8;
    --sky: #a9dde6;
    --brand-blue: #0a56a5;
    --accent-blue: #1b7fd0;
    --cyan: #3cc3ee;
    --orange: #f5a623;
    --bullet: #f26a21;
    --ink: #222;
    --dark: #0f1012;
    --dark-2: #2a2b2e;
    --steel: #8a8d92;
    --white: #ffffff;
  }
  * { box-sizing: border-box; margin: 0; padding: 0; }
  html, body { width: 959px; height: 1200px; overflow: hidden; background: var(--white); }
  .flyer { position: relative; width: 959px; height: 1200px; overflow: hidden; font-family: 'Open Sans', sans-serif; }

  .left-panel { position: absolute; left: 0; top: 0; width: 566px; height: 1200px; background: linear-gradient(180deg, var(--sky-light), #f4fbfc 60%, var(--sky) 100%); }
  .right-panel { position: absolute; left: 566px; top: 0; width: 393px; height: 1200px; background: linear-gradient(180deg, var(--dark) 0%, var(--dark) 55%, var(--dark-2) 100%); border-left: 9px solid var(--steel); }

  .header { position: absolute; left: 0; top: 0; width: 566px; height: 333px; background: linear-gradient(180deg, var(--sky) 0%, var(--sky-light) 100%); text-align: center; }
  .headline { font-family: 'Oswald', sans-serif; font-weight: 700; color: var(--brand-blue); line-height: .84; }
  .headline .line-1 { display: block; font-size: 104px; letter-spacing: 13px; margin-top: 30px; }
  .headline .line-2 { display: block; font-size: 104px; letter-spacing: 0; margin-top: 4px; }
  .header .tagline { margin-top: 20px; font-weight: 600; font-size: 19px; line-height: 27px; color: var(--ink); }

  .hero-photo { position: absolute; left: 0; top: 333px; width: 566px; height: 341px; background: linear-gradient(180deg, #c9ccd0 0%, #8f9296 45%, #b8babd 100%); }
  .service-area { position: absolute; left: 46px; top: 640px; font-weight: 600; font-size: 18px; color: var(--dark); }

  .emblem-clip { position: absolute; left: 0; top: 0; width: 575px; height: 1200px; overflow: hidden; }
  .emblem { position: absolute; left: 459px; top: 316px; width: 382px; height: 382px; border-radius: 50%; background: var(--dark); border: 10px solid var(--steel); }
  .brand-name { position: absolute; left: 575px; width: 384px; top: 472px; text-align: center; font-family: 'Nunito', sans-serif; font-weight: 800; font-size: 44px; color: var(--cyan); letter-spacing: 2px; }

  .about { position: absolute; left: 621px; top: 54px; width: 320px; font-family: 'Nunito', sans-serif; font-weight: 700; font-size: 28px; line-height: 41.5px; color: #cdeef5; }

  .warranty { position: absolute; left: 0; top: 674px; width: 566px; height: 314px; background: linear-gradient(180deg, var(--white) 0%, var(--sky-light) 100%); }
  .warranty h2 { font-family: 'Oswald', sans-serif; font-weight: 700; font-size: 38px; line-height: 44px; color: var(--accent-blue); margin: 10px 0 0 41px; letter-spacing: .5px; }
  .benefits { list-style: none; margin: 18px 0 0 40px; }
  .benefits li { position: relative; padding-left: 26px; font-size: 15px; line-height: 21.5px; color: var(--ink); }
  .benefits li::before { content: ""; position: absolute; left: 0; top: 5px; width: 12px; height: 12px; border-radius: 50%; background: var(--bullet); }

  .gallery { position: absolute; left: 0; top: 988px; width: 566px; height: 182px; background: var(--accent-blue); padding: 5px 0 6px; display: flex; gap: 6px; }
  .gallery .photo { flex: 1; }
  .photo.cabinets { background: linear-gradient(135deg, #d8d4cc, #8b8a86 60%, #2c2c2c); }
  .photo.lift-bay { background: linear-gradient(180deg, #c4c7cb, #7f8286 60%, #a8aaad); }

  .offer { position: absolute; left: 575px; width: 384px; top: 634px; text-align: center; font-family: 'Oswald', sans-serif; font-weight: 700; color: var(--orange); line-height: 1.02; }
  .offer .small { font-size: 42px; }
  .offer .big { font-size: 46px; letter-spacing: .5px; }
  .cta { position: absolute; left: 575px; width: 384px; top: 746px; text-align: center; font-size: 34px; line-height: 44px; color: var(--white); }
  .phone-banner { position: absolute; left: 603px; top: 809px; width: 320px; height: 43px; }
  .phone { position: absolute; left: 603px; top: 804px; width: 320px; text-align: center; font-family: 'Oswald', sans-serif; font-weight: 700; font-size: 34px; line-height: 50px; color: var(--white); }
  .email { position: absolute; left: 575px; width: 384px; top: 856px; text-align: center; font-size: 20px; line-height: 28px; color: var(--white); }
  .quote { position: absolute; left: 621px; top: 910px; width: 286px; font-size: 14.5px; line-height: 24.3px; color: #e9e9e9; text-align: justify; text-align-last: center; }
  .website { position: absolute; left: 575px; width: 384px; top: 1120px; text-align: center; font-family: 'Oswald', sans-serif; font-weight: 700; font-size: 42px; line-height: 60px; color: var(--cyan); }
</style>
</head>
<body>
<div class="flyer">
  <div class="left-panel"></div>
  <div class="right-panel"></div>

  <header class="header">
    <h1 class="headline"><span class="line-1">GARAGE</span><span class="line-2">FLOORING</span></h1>
    <p class="tagline">We use industrial grade products and are<br>serious about durability and quality.</p>
  </header>

  <div class="hero-photo" role="img" aria-label="Finished garage with grey flake epoxy floor, car lifts and sports cars"></div>
  <p class="service-area">Serving Southeastern Wisconsin!</p>

  <div class="emblem-clip"><div class="emblem"></div></div>
  <div class="brand-name">KORE REVIVE</div>

  <p class="about">We are KORE<br>REVIVE LLC,<br>Home of the garage<br>enthusiasts and<br>Waukesha’s premier<br>garage floor<br>installer</p>

  <section class="warranty">
    <h2>LIFETIME LIMITED WARRANTY</h2>
    <ul class="benefits">
      <li>Industrial Quality and Strength</li>
      <li>Easy to Clean</li>
      <li>Oil and Chemical Resistant</li>
      <li>Many Color Options</li>
      <li>Locally Owned and Operated</li>
      <li>Satisfaction Guaranteed</li>
      <li>Increases Home Value</li>
      <li>MAKE YOUR FRIENDS AND NEIGHBORS JEALOUS!</li>
      <li>Certified and Trusted Installer</li>
      <li>UV Stable</li>
      <li>Impact and Abrasion Resistant</li>
    </ul>
  </section>

  <div class="gallery">
    <div class="photo cabinets" role="img" aria-label="Garage with grey cabinets, glossy floor and a black sports car"></div>
    <div class="photo lift-bay" role="img" aria-label="Garage bay with car lifts and a white sports car on a flake floor"></div>
  </div>

  <div class="offer"><div class="small">for OFFERS &amp;</div><div class="big">FREE ESTIMATE</div></div>
  <p class="cta">Call or Email</p>
  <svg class="phone-banner" viewBox="0 0 320 43" aria-hidden="true"><polygon points="24,0 296,0 320,43 0,43" fill="#3cc3ee"/></svg>
  <p class="phone">012-345-6789</p>
  <p class="email">info@KoreRevive.com</p>
  <p class="quote">"From diamond grinding surface prep to using only the highest industrial-grade products, we believe in taking the time to ensure a proper installation and guarantee a durable long-lasting and beautiful garage floor"</p>
  <p class="website">KoreRevive.com</p>
</div>
</body>
</html>
```